Tall Maple website Laser Like Lipo and Facial Rejuvenation busines

I need a website for my Laser Like Lipo and Facial Rejuvenation business called Tall Maple. I purchased the domain name. I have a logo and before and after pictures to include along with basic information about the procedure and pricing information. I would like my website to be used by customers to be able to schedule appointments. My logo and before-and-after pictures are attached.

My business is called Tall Maple. It is a laser like Lipo and facial rejuvenation. I've attached my logo and before and after pictures to use on the website.

These treatments are non invasive and people lose 2-10 inches per treatment. My primary audience will be overweight women 30 years of age or older or those with cellulite. I will have some male customers too but mostly women.

As for the web design, I've never had a website before so I really don't have anything specific in mind. I'm open to considering anything. I'm not a girly, girl and I don't like frilly, fancy stuff. I just want something simple but not to either. I love my logo. That is a great fit for my business and personality. I have increased the budget to include coding.

I do not like pastel colors. I do need colors that compliment my logo.

Target Market(s)

Mostly over weight Women or those with cellulite ages 30 and above. Some men.

Industry/Entity Type

Business

Coding

Coded - Design and coding required

Number of Pages Required

3 page

Font styles to use
Serif

Requirements
Must have
• I want my logo and information section on one page, a page for before and after pictures that enlarge when clicked on. I do not want a slide show, and a page for prices. I previously mentioned a section for them to schedule appointments but have decided that I don't want that.
• I do not like pastel colors. I do need colors that compliment my logo.
Should not have
• Not a slide show

```html
<!DOCTYPE html>
<html lang="en">
<head>
<meta charset="utf-8">
<title>Tall Maple – Laser Like Lipo &amp; Facial Rejuvenation</title>
<link href="https://fonts.googleapis.com/css2?family=Courgette&family=Roboto:wght@300;400&display=swap" rel="stylesheet">
<style>
  :root {
    --page-bg: #ffffff;
    --ink: #2f2f2f;
    --muted: #8a8a8a;
    --rule: #e3e3e3;
    --accent: #c8242b;
    --accent-dark: #9e161c;
    --card-bg: #050505;
    --card-text: #ffffff;
    --skin-light: #d7b49a;
    --skin-dark: #8c6a55;
  }
  * { margin: 0; padding: 0; box-sizing: border-box; }
  html, body { width: 839px; height: 1200px; overflow: hidden; background: var(--page-bg); }
  body { position: relative; font-family: "Roboto", Arial, sans-serif; color: var(--ink); }

  .brand { position: absolute; top: 34px; left: 0; width: 839px; text-align: center; }
  .brand-name { font-family: "Roboto", Arial, sans-serif; font-weight: 400; font-size: 42px; line-height: 1; color: var(--ink); }
  .brand-tagline { margin-top: 14px; font-size: 11px; letter-spacing: 1.2px; color: var(--ink); text-transform: uppercase; }

  .main-nav { position: absolute; top: 124px; left: 60px; width: 719px; height: 52px;
    border-top: 1px solid var(--rule); border-bottom: 1px solid var(--rule);
    display: flex; justify-content: center; align-items: center; gap: 46px; font-size: 15px; }
  .main-nav a { color: var(--ink); text-decoration: none; }
  .main-nav a.current { color: var(--accent); }

  .feature-badge { position: absolute; top: 214px; left: 324px; width: 190px; height: 190px; }
  .feature-badge span { position: absolute; inset: 0; display: flex; align-items: center; justify-content: center;
    text-align: center; color: #fff; font-size: 27px; font-weight: 300; line-height: 1.25; }

  .intro { position: absolute; top: 448px; left: 170px; width: 499px; text-align: center;
    font-size: 11.5px; line-height: 1.6; color: var(--muted); }

  .results { position: absolute; top: 532px; left: 50px; width: 742px;
    display: grid; grid-template-columns: repeat(3, 222px); column-gap: 38px; row-gap: 22px; }
  .result-card { height: 280px; background: var(--card-bg); padding: 10px 10px 0; box-shadow: 0 2px 6px rgba(0,0,0,.25); }
  .result-photos { display: flex; gap: 6px; height: 112px; }
  .result-photo { flex: 1; background: linear-gradient(180deg, var(--skin-light), var(--skin-dark)); }
  .result-photo.after { background: linear-gradient(180deg, #e2c3aa, #a07e67); }
  .result-caption { font-family: "Courgette", cursive; color: var(--card-text); font-size: 17px; line-height: 1; padding: 0 10px; }
  .caption-labels { display: flex; justify-content: space-between; margin-top: 24px; }
  .caption-count { margin-top: 20px; display: flex; justify-content: space-between; }
  .caption-unit { margin-top: 20px; text-align: center; }

  .site-footer { position: absolute; top: 1152px; left: 60px; width: 719px; border-top: 1px solid var(--rule);
    padding-top: 16px; text-align: center; font-size: 11px; color: var(--muted); }
  .site-footer b { color: var(--accent); font-weight: 400; }
</style>
</head>
<body>
  <header class="brand">
    <div class="brand-name">Tall Maple</div>
    <div class="brand-tagline">Laser Like Lipo &amp; Facial Rejuvenation</div>
  </header>

  <nav class="main-nav">
    <a class="current" href="#">Home</a>
    <a href="#">About Us</a>
    <a href="#">Contact Us</a>
  </nav>

  <div class="feature-badge">
    <svg width="190" height="190" viewBox="0 0 190 190">
      <circle cx="95" cy="95" r="94" fill="var(--accent-dark)" opacity=".35"/>
      <circle cx="95" cy="95" r="88" fill="var(--accent)"/>
      <circle cx="95" cy="95" r="70" fill="none" stroke="#ffffff" stroke-opacity=".35" stroke-width="1.5"/>
    </svg>
    <span>Best<br>Selection</span>
  </div>

  <p class="intro">Lorem Ipsum is simply dummy text of the printing and typesetting industry. Lorem Ipsum has been the industry's standard dummy text ever since the 1500s, when an unknown printer took a galley of type and scrambled it to make a type specimen book.</p>

  <main class="results">
    <article class="result-card">
      <div class="result-photos">
        <div class="result-photo" role="img" aria-label="Before photo of client's torso"></div>
        <div class="result-photo after" role="img" aria-label="After photo of client's torso"></div>
      </div>
      <div class="result-caption">
        <div class="caption-labels"><span>Before</span><span>After</span></div>
        <div class="caption-count"><span>1</span><span>Laser</span><span>Like</span><span>Lipo</span></div>
        <div class="caption-unit">Treatment</div>
      </div>
    </article>
    <article class="result-card">
      <div class="result-photos">
        <div class="result-photo" role="img" aria-label="Before photo of client's torso"></div>
        <div class="result-photo after" role="img" aria-label="After photo of client's torso"></div>
      </div>
      <div class="result-caption">
        <div class="caption-labels"><span>Before</span><span>After</span></div>
        <div class="caption-count"><span>8</span><span>Laser</span><span>Like</span><span>Lipo</span></div>
        <div class="caption-unit">Treatments</div>
      </div>
    </article>
    <article class="result-card">
      <div class="result-photos">
        <div class="result-photo" role="img" aria-label="Before photo of client's body"></div>
        <div class="result-photo after" role="img" aria-label="After photo of client's body"></div>
      </div>
      <div class="result-caption">
        <div class="caption-labels"><span>Before</span><span>After</span></div>
        <div class="caption-count"><span>8</span><span>Laser</span><span>Like</span><span>Lipo</span></div>
        <div class="caption-unit">Treatments</div>
      </div>
    </article>
    <article class="result-card">
      <div class="result-photos">
        <div class="result-photo" role="img" aria-label="Before photo of client's torso"></div>
        <div class="result-photo after" role="img" aria-label="After photo of client's torso"></div>
      </div>
      <div class="result-caption">
        <div class="caption-labels"><span>Before</span><span>After</span></div>
        <div class="caption-count"><span>8</span><span>Laser</span><span>Like</span><span>Lipo</span></div>
        <div class="caption-unit">Treatments</div>
      </div>
    </article>
    <article class="result-card">
      <div class="result-photos">
        <div class="result-photo" role="img" aria-label="Before photo of client's back"></div>
        <div class="result-photo after" role="img" aria-label="After photo of client's back"></div>
      </div>
      <div class="result-caption">
        <div class="caption-labels"><span>Before</span><span>After</span></div>
        <div class="caption-count"><span>1</span><span>Laser</span><span>Like</span><span>Lipo</span></div>
        <div class="caption-unit">Treatment</div>
      </div>
    </article>
    <article class="result-card">
      <div class="result-photos">
        <div class="result-photo" role="img" aria-label="Before photo of client's body"></div>
        <div class="result-photo after" role="img" aria-label="After photo of client's body"></div>
      </div>
      <div class="result-caption">
        <div class="caption-labels"><span>Before</span><span>After</span></div>
        <div class="caption-count"><span>8</span><span>Laser</span><span>Like</span><span>Lipo</span></div>
        <div class="caption-unit">Treatments</div>
      </div>
    </article>
  </main>

  <footer class="site-footer">© <b>Tall Maple</b> - 2016, All Rights Reserved</footer>
</body>
</html>
```